Bref créative
Business Cards, Letterhead, Envelopes, Fax Cover, Email Signature, Truck
Brindle Roofing Ltd.
I need double sided standard sized Business Card [3.5" x 2"]
Do not limit yourself to font used in logo
Professional
Tomasz Oduya
42 Fairwick Lane NE
Calgary AB T3M2R8
tomi@brindleroofing.example
www.brindleroofing.example
Open to different ideas. For example : just logo, web address etc
Photograph-1 of truck
Picture 2
Picture-3
Picture-4
Picture-5
Color scheme(s)to be used for Truck

```html
<!DOCTYPE html>
<html lang="en">
<head>
<meta charset="UTF-8">
<title>Brindle Roofing Ltd. — Business Card Concepts</title>
<link href="https://fonts.googleapis.com/css2?family=Arimo:wght@400;700&display=swap" rel="stylesheet">
<style>
  :root {
    --page-bg: #ffffff;
    --card-border: #9a9a9a;
    --sage: #8cb05e;
    --sage-light: #b5d08f;
    --sage-deep: #7aa04c;
    --ink: #555555;
    --grey-center: #d8d8d8;
    --grey-edge: #8e8e8e;
    --white: #ffffff;
  }
  * { box-sizing: border-box; margin: 0; padding: 0; }
  html, body {
    width: 1200px; height: 1025px; overflow: hidden;
    background: var(--page-bg);
    font-family: "Arimo", Arial, sans-serif;
  }
  .sheet { position: relative; width: 1200px; height: 1025px; }
  .card {
    position: absolute; width: 578px; height: 322px;
    border: 1px solid var(--card-border); overflow: hidden;
  }
  .card--front-white { left: 6px; top: 6px; background: var(--white); }
  .card--back-white { left: 617px; top: 6px; background: var(--white); }
  .card--green { left: 6px; top: 347px;
    background: linear-gradient(170deg, var(--sage-deep) 0%, var(--sage) 45%, var(--sage-light) 100%); }
  .card--grey { left: 617px; top: 347px;
    background: radial-gradient(ellipse at 55% 50%, var(--grey-center) 0%, #b4b4b4 55%, var(--grey-edge) 100%); }
  .card--green-rule { left: 294px; top: 692px;
    background: linear-gradient(170deg, var(--sage-deep) 0%, var(--sage) 45%, var(--sage-light) 100%); }

  .edge-band { position: absolute; top: 0; bottom: 0; left: 0; }
  .edge-band--thin { width: 16px;
    background: linear-gradient(to top, var(--sage) 0%, var(--sage-light) 55%, #eef4e4 100%); }
  .edge-band--wide { width: 40px;
    background: linear-gradient(to right, var(--sage-light) 0%, var(--sage) 50%, var(--sage-light) 100%); }
  .accent-rule { position: absolute; top: 0; bottom: 0; left: 36px; width: 2px;
    background: rgba(255,255,255,0.55); }

  .brand { position: absolute; display: flex; align-items: center; gap: 10px;
    font-weight: 700; letter-spacing: -0.5px; white-space: nowrap; }
  .brand__dot { width: 30px; height: 30px; border-radius: 50%; flex: none; }
  .brand--sage { color: var(--sage-deep); }
  .brand--sage .brand__dot { background: var(--sage); }
  .brand--white { color: var(--white); }
  .brand--white .brand__dot { background: var(--white); }
  .brand__name { font-size: 34px; }

  .holder { position: absolute; left: 42px; top: 240px;
    font-size: 16px; font-weight: 700; color: var(--sage-deep); }
  .contact { position: absolute; left: 356px; top: 196px;
    font-size: 12.5px; line-height: 15.5px; color: var(--ink); list-style: none; }
</style>
</head>
<body>
<main class="sheet">

  <section class="card card--front-white" aria-label="Front, white">
    <div class="edge-band edge-band--thin"></div>
    <div class="brand brand--sage" style="left:46px; top:22px;">
      <span class="brand__dot"></span><span class="brand__name">brindleroofing Ltd.</span>
    </div>
    <p class="holder">Tomasz Oduya</p>
    <ul class="contact">
      <li>42 Fairwick Lane NE</li>
      <li>Calgary AB T3M2R8</li>
      <li>Phone : 5875550142</li>
      <li>Cell : 5875550178</li>
      <li>Fax : 5875550193</li>
      <li>Email : tomi@brindleroofing.example</li>
      <li>Web : www.brindleroofing.example</li>
    </ul>
  </section>

  <section class="card card--back-white" aria-label="Back, white">
    <div class="edge-band edge-band--wide"></div>
    <div class="brand brand--sage" style="left:110px; top:160px;">
      <span class="brand__dot"></span><span class="brand__name">brindleroofing Ltd.</span>
    </div>
  </section>

  <section class="card card--green" aria-label="Back, green">
    <div class="brand brand--white" style="left:100px; top:160px;">
      <span class="brand__dot"></span><span class="brand__name">brindleroofing Ltd.</span>
    </div>
  </section>

  <section class="card card--grey" aria-label="Back, grey">
    <div class="brand brand--white" style="left:100px; top:160px;">
      <span class="brand__dot"></span><span class="brand__name">brindleroofing Ltd.</span>
    </div>
  </section>

  <section class="card card--green-rule" aria-label="Back, green with rule">
    <div class="accent-rule"></div>
    <div class="brand brand--white" style="left:104px; top:168px;">
      <span class="brand__dot"></span><span class="brand__name">brindleroofing Ltd.</span>
    </div>
  </section>

</main>
</body>
</html>
```